Asia based real estate financing firm needs and AWESOME design for a biz card -Harbor Lending Circle

Looking for a stylish, & corporate-looking business card for a real estate financing brokerage firm in Asia, offering global mortgage loans. I uploaded our current logos. We would like to add a splash of color (perhaps the house icon) or any other suggestions are open. For the winning designer, we have a lot of work! Thanks and best of luck!

Target Market(s)

Real estate investors globally. We want to look more like a BANK and NOT a real estate company. Please don't play up on a "house" design.

Industry/Entity Type

Banking

Contact Information for Business Card

Harbor Lending Circle
Peter Wilks
Co-Founder | Partner

14 Cassia Lane, Suite 310
Singapore 047219
www.hlc-example.asia
peterwilks@hlc-example.asia
+65 555-0142
WeChat: peterwilks

Colors

Designer to choose colors to be used in the design.

Requirements
Must have
• Must have the standard business requirements for a card; name, address, email, etc
• Can be horizontal or vertical.
Nice to have
• It would be great to see some sort of variation to the logo with a pop of color. Red is good as we're in Asia, however, other options work as well.
• Our tag line is - Borderless mortgages. It doesn't have to be on the card but might be nice.
• I'd like to start seeing our tagline within the cards as well. - Borderless mortgages.
• Also, please add our location. The location for this card is Singapore so perhaps it can be highlighted or emphasised in some way.
• Singapore | Hong Kong | Shanghai | Manila
• As we will soon open an office in Shanghai, having an option for both languages would be great.
Should not have
• I'm exceited and open to your creativity ... knock it out of the park!

```html
<!DOCTYPE html>
<html lang="en">
<head>
<meta charset="utf-8">
<title>Harbor Lending Circle – Business Card</title>
<link href="https://fonts.googleapis.com/css2?family=Lato:wght@400;700&display=swap" rel="stylesheet">
<style>
  :root {
    --ink: #0b0b0b;
    --paper: #ffffff;
    --backdrop: #e6e6e6;
    --rule: #555555;
    --shadow: rgba(0, 0, 0, 0.18);
  }
  * { box-sizing: border-box; margin: 0; padding: 0; }
  html, body {
    width: 1200px; height: 900px; overflow: hidden;
    background: var(--backdrop);
    font-family: "Lato", Arial, sans-serif;
  }
  .stage {
    width: 1200px; height: 900px;
    display: flex; flex-direction: column; align-items: center; justify-content: center;
    gap: 48px;
  }
  .card {
    position: relative;
    width: 640px; height: 366px;
    border-radius: 22px;
    box-shadow: 0 10px 24px var(--shadow);
    overflow: hidden;
  }
  /* front */
  .card-front {
    background: var(--ink); color: var(--paper);
    display: flex; flex-direction: column; align-items: center; justify-content: center;
  }
  .brand-name {
    font-family: "Lato", Arial, sans-serif;
    font-weight: 400;
    letter-spacing: 0.14em;
    text-transform: uppercase;
    display: flex; align-items: center; gap: 14px;
  }
  .brand-mark {
    display: inline-block; width: 14px; height: 14px; border-radius: 50%;
    background: currentColor;
  }
  .card-front .brand-name { font-size: 30px; }
  .card-front .website { margin-top: 38px; font-size: 21px; letter-spacing: 0.02em; }

  /* back */
  .card-back { background: var(--paper); color: var(--ink); }
  .card-back .brand-name {
    position: absolute; left: 0; right: 0; top: 84px;
    justify-content: center; font-size: 24px;
  }
  .identity {
    position: absolute; right: 328px; top: 176px; text-align: right;
  }
  .identity .person { font-size: 22px; }
  .identity .role { font-size: 18px; margin-top: 6px; }
  .divider {
    position: absolute; left: 330px; top: 160px; width: 1px; height: 100px;
    background: var(--rule);
  }
  .contacts {
    position: absolute; left: 348px; top: 162px; list-style: none;
    font-size: 14px;
  }
  .contacts li { display: flex; align-items: center; gap: 10px; height: 24px; }
  .contacts svg { width: 14px; height: 14px; flex: none; fill: var(--ink); }
  .address-band {
    position: absolute; left: 0; right: 0; top: 290px; height: 40px;
    background: var(--ink); color: var(--paper);
    display: flex; align-items: center; justify-content: center;
    font-weight: 700; font-size: 18px; letter-spacing: 0.01em;
  }
</style>
</head>
<body>
<main class="stage">
  <section class="card card-front">
    <div class="brand-name"><span class="brand-mark"></span>Harbor Lending Circle</div>
    <p class="website">www.hlc-example.asia</p>
  </section>

  <section class="card card-back">
    <div class="brand-name"><span class="brand-mark"></span>Harbor Lending Circle</div>
    <div class="identity">
      <p class="person">Peter Wilks</p>
      <p class="role">Co-Founder | Partner</p>
    </div>
    <div class="divider"></div>
    <ul class="contacts">
      <li><svg viewBox="0 0 16 16" aria-hidden="true"><path d="M3.5 1.5l2.5 2.5-1.5 2a9 9 0 0 0 5.5 5.5l2-1.5 2.5 2.5-2 2C6.5 14.5 1.5 9.5 1.5 3.5z"/></svg>+65 555-0142</li>
      <li><svg viewBox="0 0 16 16" aria-hidden="true"><path d="M1 3h14v10H1z M1 3l7 6 7-6" fill="none" stroke="#0b0b0b" stroke-width="1.6"/><path d="M1 3h14L8 9z"/></svg>peterwilks@hlc-example.asia</li>
      <li><svg viewBox="0 0 16 16" aria-hidden="true"><circle cx="8" cy="8" r="6.5" fill="none" stroke="#0b0b0b" stroke-width="1.6"/><path d="M1.5 8h13M8 1.5c-3 3.5-3 9.5 0 13M8 1.5c3 3.5 3 9.5 0 13" fill="none" stroke="#0b0b0b" stroke-width="1.2"/></svg>www.hlc-example.asia</li>
      <li><svg viewBox="0 0 16 16" aria-hidden="true"><circle cx="8" cy="8" r="6.5" fill="none" stroke="#0b0b0b" stroke-width="1.6"/></svg>peterwilks</li>
    </ul>
    <div class="address-band">14 Cassia Lane, Suite 310 Singapore 047219</div>
  </section>
</main>
</body>
</html>
```